Harbor Home Care Agency Needs a Website (Seeking a PSD)

We need a user friendly website for a Harbor Home Care Agency. Our service is for the elderly and disabled. Frequently the busy professional middle-aged married daughter will use the website to arrange in-home care for an aging parent. Therefore, our website is primarily geared towards middle-aged women. In-home care is typically 24 hours a day so, a feeling of trustworthiness and security should be effectively conveyed. (Seeking a PSD- however, if you also offer coding, please let us know the cost.)

Target Market(s)

Frequently the busy professional middle-aged married daughter (possibly out of state) will use the website to arrange in-home care for an aging parent.

Industry/Entity Type

Security

Requirements
Must have
• Website must be clean, uncluttered and professional. The following menu pages are requested: Home, About Us, Services, Resources, FAQ, Employment & Contact.
Should not have
• Must not be too whimsical.

```html
<!DOCTYPE html>
<html lang="en">
<head>
<meta charset="utf-8">
<title>Harbor Home Care</title>
<link href="https://fonts.googleapis.com/css2?family=Noto+Sans:wght@400;700&family=Noto+Serif:ital@1&family=Raleway:wght@300;400&display=swap" rel="stylesheet">
<style>
:root{
  --blue:#4bc3ee;
  --blue-dark:#2aa9dd;
  --ink:#222;
  --grey:#5e6166;
  --light:#f5f5f5;
  --line:#d6d6d6;
}
*{box-sizing:border-box;margin:0;padding:0}
html,body{width:1056px;height:1200px;overflow:hidden;background:#fff}
body{position:relative;font-family:"Noto Sans",sans-serif;color:var(--ink)}
.abs{position:absolute}

.topline{left:0;top:0;width:1056px;height:3px;background:var(--grey)}
.brand{left:106px;top:16px;display:flex;align-items:center;gap:6px;color:var(--blue);font-weight:700;font-size:17px;line-height:1.05}
.brand .dot{width:22px;height:22px;border-radius:50%;background:var(--blue)}
.hotline{right:106px;top:37px;font-size:11.5px}
.hotline b{font-weight:400;color:var(--blue);font-size:15px}

.nav{left:0;top:83px;width:1056px;height:41px;background:linear-gradient(#7fd6f5,#3fbaea);border-top:1px solid #9fe0f8}
.nav a{position:absolute;top:0;height:41px;line-height:41px;text-align:center;color:#fff;font-size:11.5px;text-decoration:none;border-right:1px solid #35a7d6}
.nav a.active{background:linear-gradient(#3a3a3a,#111)}
.search{left:734px;top:89px;width:201px;height:28px;border-radius:14px;background:#fff;box-shadow:inset 0 1px 2px rgba(0,0,0,.2)}

.hero{left:0;top:124px;width:1056px;height:372px;background:linear-gradient(90deg,#e3d8d0,#f3f2ef 45%,#d6c7bb)}
.hero-title{left:356px;top:350px;font-size:33px;font-family:"Noto Sans",sans-serif;color:#000}
.hero-title i{font-style:italic}
.hero-band{left:384px;top:404px}
.hero-cta{left:472px;top:418px;color:#fff;font-weight:700;font-size:25px;letter-spacing:.3px;text-shadow:0 1px 3px rgba(0,0,0,.35)}

.services-photo{left:90px;top:528px}
.section-title{font-family:"Raleway",sans-serif;font-weight:300;font-size:23px;color:#333}
.svc-title{font-family:"Raleway",sans-serif;font-size:17px;color:#222}
.svc-body{font-family:"Noto Serif",serif;font-style:italic;font-size:12px;line-height:20.6px;color:#333;width:230px}
.svc-icon{width:20px;height:24px}
.arrows{left:898px;top:729px;display:flex}
.arrows span{width:26px;height:25px;display:block}

.testimonial{left:0;top:790px;width:1056px;height:169px;background:var(--light)}
.t-photo{left:107px;top:822px;width:104px;height:104px;background:#fff;border:1px solid #ddd;box-shadow:0 1px 3px rgba(0,0,0,.15);padding:4px}
.t-photo div{width:100%;height:100%;background:linear-gradient(135deg,#9cb4c9,#d9b9a2 55%,#6c8aa8)}
.t-line{left:229px;top:822px;width:1px;height:104px;background:var(--line)}
.quote-mark{left:246px;top:808px;font-family:"Noto Serif",serif;font-size:34px;color:#bbb}
.t-text{left:278px;top:836px;width:660px;font-family:"Noto Serif",serif;font-style:italic;font-size:12.3px;line-height:20.6px;color:#333}
.t-name{left:278px;top:898px;font-family:"Noto Serif",serif;font-size:12.3px;color:#333}

.footer{left:0;top:959px;width:1056px;height:241px;background:linear-gradient(#44484d,#000);border-top:3px solid var(--blue)}
.f-head{font-family:"Raleway",sans-serif;font-size:18px;color:#fff}
.field{background:#fff;font-size:11.5px;color:#444;padding:7px 8px}
.send{left:106px;top:1147px;width:82px;height:29px;background:linear-gradient(#6fd0f3,#2fb0e4);border:1px solid #9fe3fb;color:#fff;font-weight:700;font-size:11px;text-align:center;line-height:27px;letter-spacing:.5px}
.follow{left:411px;top:1021px}
.follow li{list-style:none;display:flex;align-items:center;height:37px;color:#fff;font-size:11.5px}
.follow .ico{width:24px;height:24px;border-radius:50%;background:#fff;margin-right:13px}
.f-brand{right:106px;top:1000px;display:flex;align-items:center;gap:10px;color:var(--blue);font-weight:700;font-size:36px;line-height:1.02;text-align:right}
.f-brand .dot{width:40px;height:40px;border-radius:50%;background:var(--blue)}
.copy{right:106px;top:1126px;color:#fff;font-size:10.5px;text-align:right}
.legal{right:106px;top:1145px;color:#fff;font-size:10.5px}
.legal a{color:var(--blue);text-decoration:none}
</style>
</head>
<body>
<div class="abs topline"></div>

<header>
  <div class="abs brand"><span class="dot"></span><span>Harbor<br>Home Care</span></div>
  <div class="abs hotline">Available <b>24/7</b> call now <b>(555) 014-2297</b></div>
</header>

<nav class="abs nav">
  <a class="active" style="left:106px;width:74px">Home</a>
  <a style="left:180px;width:92px">About Us</a>
  <a style="left:272px;width:87px">Services</a>
  <a style="left:359px;width:98px">Resources</a>
  <a style="left:457px;width:66px">FAQ</a>
  <a style="left:523px;width:111px">Employment</a>
  <a style="left:634px;width:85px">Contact</a>
</nav>
<div class="abs search">
  <svg class="abs" style="right:10px;top:6px" width="16" height="16" viewBox="0 0 16 16"><circle cx="6" cy="6" r="4.3" fill="none" stroke="#555" stroke-width="1.8"/><line x1="9.2" y1="9.2" x2="14.5" y2="14.5" stroke="#555" stroke-width="2.6" stroke-linecap="round"/></svg>
</div>

<section class="abs hero" role="img" aria-label="Smiling caregiver facing an elderly woman"></section>
<div class="abs hero-title">We take care <i>your family</i> as <i>our family</i></div>
<svg class="abs hero-band" width="672" height="62" viewBox="0 0 672 62">
  <polygon points="0,0 672,0 672,62 62,62" fill="#fff" opacity=".75"/>
  <polygon points="12,2 672,2 672,56 62,56" fill="#5ec8ef"/>
</svg>
<div class="abs hero-cta">CLICK FOR OUR HOME HEALTH SERVICES</div>

<section>
  <svg class="abs services-photo" width="150" height="230" viewBox="0 0 150 230">
    <path d="M131,5 A110,110 0 0 0 131,225" fill="none" stroke="var(--blue)" stroke-width="11"/>
  </svg>
  <div class="abs" role="img" aria-label="Two women reading together and smiling" style="left:132px;top:552px;width:182px;height:182px;border-radius:50%;background:radial-gradient(circle at 40% 40%,#f1e7e2,#e4a49a 60%,#c98b7d)"></div>

  <h2 class="abs section-title" style="left:348px;top:533px">OUR SERVICES</h2>

  <svg class="abs svc-icon" style="left:349px;top:582px" viewBox="0 0 20 24"><path d="M12,2 A10,10 0 0 0 12,22" fill="none" stroke="var(--blue)" stroke-width="2.2"/><circle cx="13" cy="12" r="4.5" fill="var(--blue)"/></svg>
  <h3 class="abs svc-title" style="left:384px;top:584px">Name of service</h3>
  <p class="abs svc-body" style="left:385px;top:612px">Lorem ipsum dolor sit amet, consectetur adipisicing elit, sed do eiusmod tempor incididunt ut labore et dolore magna aliqua. Ut enim ad minim veniam, quis nostrud exercitation.</p>

  <svg class="abs svc-icon" style="left:662px;top:582px" viewBox="0 0 20 24"><path d="M12,2 A10,10 0 0 0 12,22" fill="none" stroke="var(--blue)" stroke-width="2.2"/><circle cx="13" cy="12" r="4.5" fill="var(--blue)"/></svg>
  <h3 class="abs svc-title" style="left:698px;top:584px">Name of service</h3>
  <p class="abs svc-body" style="left:699px;top:612px">Lorem ipsum dolor sit amet, consectetur adipisicing elit, sed do eiusmod tempor incididunt ut labore et dolore magna aliqua. Ut enim ad minim veniam, quis nostrud exercitation.</p>

  <div class="abs arrows">
    <span style="background:#000"><svg width="26" height="25"><polyline points="15,7 10,12.5 15,18" fill="none" stroke="#fff" stroke-width="3"/></svg></span>
    <span style="background:var(--blue)"><svg width="26" height="25"><polyline points="11,7 16,12.5 11,18" fill="none" stroke="#fff" stroke-width="3"/></svg></span>
  </div>
</section>

<section class="abs testimonial"></section>
<div class="abs t-photo"><div role="img" aria-label="Portrait of a smiling elderly man"></div></div>
<div class="abs t-line"></div>
<svg class="abs" style="left:228px;top:866px" width="8" height="14"><polyline points="1,0 7,7 1,14" fill="var(--light)" stroke="var(--line)"/></svg>
<div class="abs quote-mark">“</div>
<p class="abs t-text">Lorem ipsum dolor sit amet, consectetur adipisicing elit, sed do eiusmod tempor incididunt ut labore et dolore magna aliqua. Ut enim ad minim veniam, quis nostrud exercitation ullamco laboris nisi ut aliquip ex ea commodo consequat. Duis aute irure dolor in reprehenderit in voluptate velit esse cillum dolore eu fugiat nulla pariatur.</p>
<div class="abs t-name"><b>Walter Brenn</b>, 65 years</div>

<footer class="abs footer"></footer>
<h2 class="abs f-head" style="left:106px;top:983px">SEND US MESSAGE</h2>
<div class="abs field" style="left:106px;top:1023px;width:231px;height:29px">E-mail</div>
<div class="abs field" style="left:106px;top:1060px;width:231px;height:78px">Message</div>
<div class="abs send">SEND</div>

<h2 class="abs f-head" style="left:411px;top:983px">FOLLOW US</h2>
<ul class="abs follow">
  <li><span class="ico"></span>Like our page on Circlebook</li>
  <li><span class="ico"></span>Follow us on Chirper</li>
  <li><span class="ico"></span>Watch our vide on ViewTube</li>
  <li><span class="ico"></span>Get RSS latest update</li>
</ul>

<div class="abs f-brand"><span class="dot"></span><span>Harbor<br>Home Care</span></div>
<div class="abs copy">Copyright (c) 2013 Harbor Home Care. All rights reserved.</div>
<div class="abs legal"><a>Privacy &amp; Policy</a> &nbsp;|&nbsp; <a>Terms &amp; Conditions</a></div>
</body>
</html>
```